Business card for law firm

Need business card for new law firm. Think confident, authoritative, conservative, but not stuffy or old-fashioned.

Contact Information for Business Card

Content for card - logo (uploaded), plus the following:

Paul Wexbury (larger font)
Managing Partner (larger font, but not as large as name)
Level 9, 41 Tansy Lane
Sydney NSW 2000
Main Tel 02 7346 2190
Direct Tel 02 6273 4415
Email paul@qvlegal.com.au
www.qvlegal.com.au

Letterhead design should include logo plus:
Level 9, 41 Tansy Lane
Sydney NSW 2000
Tel 02 6273 4415
www.qvlegal.com.au

```html
<!DOCTYPE html>
<html lang="en">
<head>
<meta charset="utf-8">
<title>Quillvane Legal — Business Card</title>
<link href="https://fonts.googleapis.com/css2?family=Cinzel:wght@400;500&family=Open+Sans:wght@400&display=swap" rel="stylesheet">
<style>
  :root {
    --navy: #041a55;
    --navy-soft: #1d3578;
    --paper: #ffffff;
    --ink: #111111;
    --backdrop: #5b5b5b;
  }
  * { box-sizing: border-box; margin: 0; padding: 0; }
  html, body {
    width: 1200px;
    height: 802px;
    overflow: hidden;
    background: var(--backdrop);
  }
  .canvas {
    position: relative;
    width: 1200px;
    height: 802px;
  }
  .card {
    position: absolute;
    top: 274px;
    width: 443px;
    height: 265px;
    background: var(--paper);
    overflow: hidden;
  }
  .card--front { left: 136px; }
  .card--back { left: 624px; }

  .feature-area {
    position: absolute;
    top: 0;
    left: 0;
    width: 237px;
    height: 100%;
    background: linear-gradient(135deg, var(--paper) 0%, #c9d0e2 30%, var(--navy-soft) 62%, var(--navy) 100%);
  }

  .contact-panel {
    position: absolute;
    top: 0;
    right: 0;
    width: 206px;
    height: 100%;
    background: var(--navy);
    color: var(--paper);
    font-family: "Open Sans", sans-serif;
    text-align: right;
    padding: 62px 24px 0 0;
  }
  .person-name {
    font-family: "Cinzel", serif;
    font-weight: 500;
    font-size: 19.5px;
    line-height: 21px;
    letter-spacing: 0.01em;
    white-space: nowrap;
  }
  .person-role {
    font-size: 13.5px;
    line-height: 15px;
    margin-bottom: 6px;
  }
  .contact-list { list-style: none; }
  .contact-line {
    font-size: 13.5px;
    line-height: 16px;
    display: flex;
    justify-content: flex-end;
    align-items: center;
    gap: 3px;
    white-space: nowrap;
  }
  .contact-line small {
    font-size: 10px;
    letter-spacing: 0.02em;
  }
  .contact-icon {
    width: 9px;
    height: 9px;
    flex: none;
    fill: var(--paper);
  }
  .address {
    font-style: normal;
    font-size: 13.5px;
    line-height: 16px;
    margin-top: 3px;
    white-space: nowrap;
  }

  .brand {
    position: absolute;
    left: 0;
    right: 0;
    top: 65px;
    display: flex;
    flex-direction: column;
    align-items: center;
    color: var(--ink);
    font-family: "Cinzel", serif;
    font-weight: 400;
  }
  .brand-square {
    width: 58px;
    height: 58px;
    background: var(--navy);
    margin-bottom: 28px;
  }
  .brand-name {
    font-size: 36px;
    line-height: 36px;
    letter-spacing: 0.02em;
  }
  .brand-tag {
    font-size: 11.5px;
    line-height: 14px;
    letter-spacing: 1.05em;
    margin-top: 2px;
    margin-right: -1.05em;
    color: var(--ink);
  }
</style>
</head>
<body>
<main class="canvas">

  <section class="card card--front" aria-label="Business card, contact side">
    <div class="feature-area" role="img" aria-label="Large brand symbol decoration in navy and white"></div>
    <div class="contact-panel">
      <h1 class="person-name">PAUL WEXBURY</h1>
      <p class="person-role">Managing Partner</p>
      <ul class="contact-list">
        <li class="contact-line">02 7346 2190
          <svg class="contact-icon" viewBox="0 0 10 10" aria-hidden="true"><path d="M1 3.2C1 2 2.5 1.5 5 1.5S9 2 9 3.2V4H7V3H3V4H1Z"/><path d="M2.5 4.5H7.5L8.8 8.5H1.2Z"/></svg>
        </li>
        <li class="contact-line">02 6273 4415 <small>(DIRECT)</small>
          <svg class="contact-icon" viewBox="0 0 10 10" aria-hidden="true"><path d="M1 3.2C1 2 2.5 1.5 5 1.5S9 2 9 3.2V4H7V3H3V4H1Z"/><path d="M2.5 4.5H7.5L8.8 8.5H1.2Z"/></svg>
        </li>
        <li class="contact-line">paul@qvlegal.com.au
          <svg class="contact-icon" viewBox="0 0 10 10" aria-hidden="true"><path d="M0.5 2H9.5V8H0.5Z"/><path d="M0.8 2.3L5 5.6L9.2 2.3" fill="none" stroke="#041a55" stroke-width="0.9"/></svg>
        </li>
        <li class="contact-line">www.qvlegal.com.au
          <svg class="contact-icon" viewBox="0 0 10 10" aria-hidden="true"><circle cx="5" cy="5" r="4.5"/><path d="M5 0.8V9.2M0.8 5H9.2" stroke="#041a55" stroke-width="0.8"/></svg>
        </li>
      </ul>
      <address class="address">
        Level 9, 41 Tansy Lane<br>
        Sydney NSW 2000
      </address>
    </div>
  </section>

  <section class="card card--back" aria-label="Business card, brand side">
    <div class="brand">
      <span class="brand-square" aria-hidden="true"></span>
      <p class="brand-name">QUILLVANE</p>
      <p class="brand-tag">LEGAL</p>
    </div>
  </section>

</main>
</body>
</html>
```